social interest sharing site needs a web site design

we need a web site design for a social web platform.
the site is one page(main page), that is split into 3 sections
each section is a different color(red,green and blue)
and a user can choose to share each of the sections.
any section/color will contain boxes , each box can contain different media types.

the media types:
* list of URLS
* list of articles including title + image + description
* list of videos
* thumbnails of images
* calender
* list of emails

the main content will look like quiltboard layout
multiple boxes each box can contain different type of content as described above

each color is a different tab
each tab will have layout like quiltboard
Updates

please read the last description update.
and i uploaded an image that can explain the requirements better

thanks
Oren

```html
<!DOCTYPE html>
<html lang="en">
<head>
<meta charset="utf-8">
<title>Huebox.me – My Home page</title>
<link href="https://fonts.googleapis.com/css2?family=Montserrat:wght@400;500;600&family=Oswald:wght@400&family=Arimo:wght@400&display=swap" rel="stylesheet">
<style>
  :root {
    --header-bg: #4a4a4a;
    --footer-bg: #3a3a3a;
    --page-red: #ff7877;
    --card-bg: #ffffff;
    --media-grey: #b8b0aa;
    --frame-grey: #8a8f94;
    --image-fill: #6a9fb4;
    --caption-teal: #1b98a5;
    --heading-red: #c9323c;
    --body-text: #3a3a3a;
    --play-red: #e05644;
    --play-shade: #c94a3b;
    --footer-text: #d8d8d8;
  }
  * { box-sizing: border-box; margin: 0; padding: 0; }
  html, body { width: 1200px; height: 1022px; overflow: hidden; }
  body { position: relative; background: var(--page-red); font-family: "Arimo", Arial, sans-serif; }

  .site-header {
    position: absolute; left: 0; top: 0; width: 1200px; height: 112px;
    background: var(--header-bg); border-bottom: 3px solid #fff;
  }
  .brand {
    position: absolute; left: 104px; top: 30px;
    display: flex; align-items: center; gap: 12px;
    font-family: "Montserrat", sans-serif; font-weight: 600; font-size: 40px;
    color: #fff; line-height: 1;
  }
  .brand-square { width: 40px; height: 40px; background: var(--page-red); }
  .social { position: absolute; left: 805px; top: 13px; display: flex; gap: 5px; }
  .social span {
    width: 37px; height: 37px; border-radius: 50%;
    background: #3b3b3b; border: 2px solid #2a2a2a;
  }
  .account-nav {
    position: absolute; left: 780px; top: 62px; display: flex; gap: 18px;
    font-family: "Oswald", sans-serif; font-size: 21px; color: #fff; letter-spacing: 0.3px;
  }

  .page-title {
    position: absolute; left: 73px; top: 145px;
    font-family: "Montserrat", sans-serif; font-weight: 500; font-size: 32px; color: #fff;
  }

  .card { position: absolute; background: var(--card-bg); overflow: hidden; }
  .media {
    margin: 13px 13px 0; height: 125px; background: var(--media-grey);
    display: flex; align-items: center; justify-content: center;
  }
  .photo-frame {
    width: 108px; height: 82px; padding: 4px; background: var(--frame-grey);
    box-shadow: 1px 2px 3px rgba(0,0,0,.35);
  }
  .photo-fill { width: 100%; height: 100%; background: var(--image-fill); }
  .caption {
    margin: 18px 0 0 23px; font-family: "Montserrat", sans-serif; font-weight: 500;
    font-size: 14.5px; letter-spacing: 0.8px; color: var(--caption-teal);
  }
  .card-heading {
    font-family: "Montserrat", sans-serif; font-weight: 500; font-size: 25px; color: var(--heading-red);
  }
  .media-card .card-heading { margin: 14px 0 0 23px; }
  .card-body {
    margin: 9px 16px 0 25px; font-size: 12.3px; line-height: 21.3px; color: var(--body-text);
  }
  .date { margin: 8px 0 0 23px; font-size: 12.5px; color: var(--caption-teal); }
  .text-card .card-heading { margin: 21px 0 0 23px; }
  .text-card .card-body { margin-top: 12px; margin-right: 12px; }
  .site-footer {
    position: absolute; left: 0; top: 947px; width: 1200px; height: 75px; background: var(--footer-bg);
  }
  .site-footer p {
    position: absolute; left: 118px; top: 13px; font-size: 11px; color: var(--footer-text); letter-spacing: 0.3px;
  }
  .site-footer a { color: var(--footer-text); text-decoration: none; margin-left: 8px; }
</style>
</head>
<body>

<header class="site-header">
  <div class="brand"><span class="brand-square"></span>Huebox.me</div>
  <div class="social" aria-label="Social links"><span></span><span></span></div>
  <nav class="account-nav"><span>LOGIN</span><span>SIGNUP</span></nav>
</header>

<h1 class="page-title">My Home page</h1>

<article class="card media-card" style="left:69px; top:206px; width:413px; height:345px;">
  <div class="media">
    <div class="photo-frame"><div class="photo-fill" role="img" aria-label="Image thumbnail placeholder"></div></div>
  </div>
  <p class="caption">image caption</p>
  <h2 class="card-heading">Heading</h2>
  <p class="card-body">Lorem ipsum dolor sit amet, consectetur adipisicing elit, sed do eiusmod tempor incididunt ut labore et dolore magna aliqua. Ut enim ad minim veniam, quis nostrud exercitation ullamco laboris nisi ut aliquip ex ea commodo consequat. Duis aute irure dolor in reprehenderit in voluptate velit esse cillum dolore eu fugiat nulla</p>
</article>

<article class="card media-card" style="left:495px; top:206px; width:280px; height:345px;">
  <div class="media">
    <svg class="play-icon" width="98" height="98" viewBox="0 0 98 98" aria-hidden="true">
      <defs><clipPath id="pc1"><circle cx="49" cy="49" r="49"/></clipPath></defs>
      <circle cx="49" cy="49" r="49" fill="var(--play-red)"/>
      <polygon points="98,0 98,98 0,98" fill="var(--play-shade)" clip-path="url(#pc1)"/>
      <polygon points="36,28 36,70 72,49" fill="#f4f1ee" stroke="#f4f1ee" stroke-width="6" stroke-linejoin="round"/>
    </svg>
  </div>
  <p class="caption">video caption</p>
  <h2 class="card-heading">Heading</h2>
  <p class="card-body">Lorem ipsum dolor sit amet, consectetur adipisicing elit, sed do eiusmod tempor incididunt ut labore et dolore magna aliqua. Ut enim ad minim veniam, quis nostrud exercitation ullamco laboris nisi</p>
</article>

<article class="card text-card" style="left:788px; top:206px; width:333px; height:345px;">
  <h2 class="card-heading">Heading</h2>
  <p class="date">20 December 2013</p>
  <p class="card-body">Lorem ipsum dolor sit amet, consectetur adipisicing elit, sed do eiusmod tempor incididunt ut labore et dolore magna aliqua. Ut enim ad minim veniam, quis nostrud exercitation ullamco laboris nisi ut aliquip ex ea commodo consequat. Duis aute irure dolor in reprehenderit in voluptate velit esse cillum dolore eu fugiat nulla pariatur. Excepteur sint occaecat cupidatat non proident, sunt in culpa qui officia deserunt mollit anim id est laborum.</p>
</article>

<article class="card text-card" style="left:69px; top:565px; width:333px; height:299px;">
  <h2 class="card-heading">Heading</h2>
  <p class="date">20 December 2013</p>
  <p class="card-body">Lorem ipsum dolor sit amet, consectetur adipisicing elit, sed do eiusmod tempor incididunt ut labore et dolore magna aliqua. Ut enim ad minim veniam, quis nostrud exercitation ullamco laboris nisi ut aliquip ex ea commodo consequat. Duis aute irure dolor in reprehenderit in voluptate velit esse cillum dolore eu fugiat nulla pariatur. Excepteur sint occaecat cupidatat non proident, sunt in culpa qui officia deserunt mollit anim id est laborum.</p>
</article>

<article class="card media-card" style="left:415px; top:565px; width:413px; height:346px;">
  <div class="media">
    <svg class="play-icon" width="107" height="107" viewBox="0 0 98 98" aria-hidden="true">
      <defs><clipPath id="pc2"><circle cx="49" cy="49" r="49"/></clipPath></defs>
      <circle cx="49" cy="49" r="49" fill="var(--play-red)"/>
      <polygon points="98,0 98,98 0,98" fill="var(--play-shade)" clip-path="url(#pc2)"/>
      <polygon points="36,28 36,70 72,49" fill="#f4f1ee" stroke="#f4f1ee" stroke-width="6" stroke-linejoin="round"/>
    </svg>
  </div>
  <p class="caption">video caption</p>
  <h2 class="card-heading">Heading</h2>
  <p class="card-body">Lorem ipsum dolor sit amet, consectetur adipisicing elit, sed do eiusmod tempor incididunt ut labore et dolore magna aliqua. Ut enim ad minim veniam, quis nostrud exercitation ullamco laboris nisi ut aliquip ex ea commodo consequat. Duis aute irure dolor in reprehenderit in voluptate velit esse cillum dolore eu fugiat nulla</p>
</article>

<article class="card media-card" style="left:841px; top:565px; width:280px; height:346px;">
  <div class="media">
    <svg class="play-icon" width="98" height="98" viewBox="0 0 98 98" aria-hidden="true">
      <defs><clipPath id="pc3"><circle cx="49" cy="49" r="49"/></clipPath></defs>
      <circle cx="49" cy="49" r="49" fill="var(--play-red)"/>
      <polygon points="98,0 98,98 0,98" fill="var(--play-shade)" clip-path="url(#pc3)"/>
      <polygon points="36,28 36,70 72,49" fill="#f4f1ee" stroke="#f4f1ee" stroke-width="6" stroke-linejoin="round"/>
    </svg>
  </div>
  <p class="caption">video caption</p>
  <h2 class="card-heading">Heading</h2>
  <p class="card-body">Lorem ipsum dolor sit amet, consectetur adipisicing elit, sed do eiusmod tempor incididunt ut labore et dolore magna aliqua. Ut enim ad minim veniam, quis nostrud exercitation ullamco laboris nisi</p>
</article>

<footer class="site-footer">
  <p>© Huebox. All rights reserved. <a href="#">Privacy Policy</a> <a href="#">Terms &amp; Conditions</a></p>
</footer>

</body>
</html>
```